Breezeway Climate Business Card Design

Design new, 2 sides, business cards for a residential and light commercial heating, air conditioning contractor.

Target Market(s)

Homeowners, small businesses

Industry/Entity Type

Business

Contact Information for Business Card

Dominic Vasquerelli
Phone - 555-214-6837
Email
Address - PO box 618
Millbrook NJ 07999
Website - www.BreezewayClimateLLC.example

Requirements
Must have
• logo, company colors, standard size with no die cut, so I can use printhaven

```html
<!DOCTYPE html>
<html lang="en">
<head>
<meta charset="utf-8">
<title>Breezeway Climate Business Card</title>
<link href="https://fonts.googleapis.com/css2?family=Open+Sans:wght@400;600;700&display=swap" rel="stylesheet">
<style>
  :root {
    --stage: #2a2c30;
    --card-white: #ffffff;
    --brand-red: #a02230;
    --brand-orange: #f39a1e;
    --ink: #2b2b2b;
    --muted: #7a7a7a;
    --band-text: #f4dfe1;
  }
  * { margin: 0; padding: 0; box-sizing: border-box; }
  html, body {
    width: 1200px; height: 900px; overflow: hidden;
    background: var(--stage);
    font-family: "Open Sans", Arial, sans-serif;
  }
  .stage {
    position: relative; width: 1200px; height: 900px;
    display: flex; flex-direction: column; align-items: center; justify-content: center; gap: 60px;
  }
  .card {
    position: relative; width: 630px; height: 360px;
    border-radius: 26px; overflow: hidden;
  }

  /* Front side */
  .card-front { background: var(--card-white); }
  .front-band {
    position: absolute; left: 0; right: 0; bottom: 0; height: 92px;
    background: var(--brand-red);
  }
  .front-rule { position: absolute; left: 0; right: 0; height: 5px; background: var(--brand-red); }
  .front-rule.outer { bottom: 104px; }
  .front-rule.inner { bottom: 116px; }
  .address {
    position: absolute; left: 48px; bottom: 34px;
    display: flex; align-items: center; gap: 10px;
    color: var(--band-text); font-size: 17px; letter-spacing: 0.3px;
  }
  .identity { position: absolute; left: 48px; top: 42px; display: flex; gap: 14px; }
  .identity-bars { display: flex; gap: 5px; padding-top: 4px; }
  .identity-bars span { width: 5px; height: 44px; background: var(--brand-red); }
  .person-name {
    font-size: 28px; font-weight: 700; letter-spacing: 1px; color: var(--ink); line-height: 1.1;
    white-space: nowrap;
  }
  .person-name .surname { color: var(--brand-red); font-weight: 600; }
  .person-title { font-size: 16px; color: var(--muted); margin-top: 2px; }
  .contact-list {
    position: absolute; left: 52px; top: 128px; list-style: none;
    font-size: 15px; color: var(--ink); line-height: 28px;
  }
  .contact-list li { display: flex; align-items: center; gap: 12px; white-space: nowrap; }
  .contact-list svg { width: 16px; height: 16px; flex: none; }
  .front-logo {
    position: absolute; right: 36px; bottom: 150px;
    display: flex; align-items: center; gap: 8px;
    font-size: 20px; font-weight: 700; color: var(--brand-red); white-space: nowrap;
  }
  .logo-dot { width: 14px; height: 14px; border-radius: 50%; background: var(--brand-orange); }

  /* Back side */
  .card-back { background: var(--brand-red); }
  .back-logo {
    position: absolute; left: 0; right: 0; top: 120px;
    display: flex; align-items: center; justify-content: center; gap: 12px;
    font-size: 40px; font-weight: 700; color: var(--brand-orange);
  }
  .back-logo .logo-dot { width: 22px; height: 22px; }
  .back-rule { position: absolute; left: 0; right: 0; height: 4px; background: var(--brand-orange); }
  .back-rule.first { bottom: 42px; }
  .back-rule.second { bottom: 30px; }
</style>
</head>
<body>
<main class="stage">
  <section class="card card-front" aria-label="Business card front">
    <div class="identity">
      <div class="identity-bars"><span></span><span></span></div>
      <div>
        <h1 class="person-name">DOMINIC <span class="surname">VASQUERELLI</span></h1>
        <p class="person-title">CEO &amp; Founder</p>
      </div>
    </div>
    <ul class="contact-list">
      <li>
        <svg viewBox="0 0 16 16" aria-hidden="true"><path d="M4 1.5l2.5 3-1.5 1.5c.8 2 2.5 3.7 4.5 4.5L11 9l3 2.5-1.5 2.5C7 14 2 9 2 3z" fill="none" stroke="#a02230" stroke-width="1.3"/></svg>
        555-214-6837
      </li>
      <li>
        <svg viewBox="0 0 16 16" aria-hidden="true"><rect x="1.5" y="3.5" width="13" height="9" fill="none" stroke="#a02230" stroke-width="1.3"/><path d="M1.5 3.5L8 9l6.5-5.5" fill="none" stroke="#a02230" stroke-width="1.3"/></svg>
        dominic@breezewayclimate.example
      </li>
      <li>
        <svg viewBox="0 0 16 16" aria-hidden="true"><circle cx="8" cy="8" r="6.5" fill="none" stroke="#a02230" stroke-width="1.3"/><ellipse cx="8" cy="8" rx="3" ry="6.5" fill="none" stroke="#a02230" stroke-width="1.1"/><path d="M1.5 8h13" stroke="#a02230" stroke-width="1.1"/></svg>
        www.BreezewayClimateLLC.example
      </li>
    </ul>
    <div class="front-logo"><span class="logo-dot"></span>Breezeway Climate</div>
    <div class="front-rule inner"></div>
    <div class="front-rule outer"></div>
    <div class="front-band"></div>
    <p class="address">
      <svg width="16" height="18" viewBox="0 0 16 18" aria-hidden="true"><path d="M8 17s-5.5-6-5.5-10a5.5 5.5 0 0 1 11 0C13.5 11 8 17 8 17z" fill="none" stroke="#f4dfe1" stroke-width="1.3"/><circle cx="8" cy="7" r="2" fill="none" stroke="#f4dfe1" stroke-width="1.3"/></svg>
      PO box 618, Millbrook NJ 07999
    </p>
  </section>

  <section class="card card-back" aria-label="Business card back">
    <div class="back-logo"><span class="logo-dot"></span>Breezeway Climate</div>
    <div class="back-rule first"></div>
    <div class="back-rule second"></div>
  </section>
</main>
</body>
</html>
```